Agriculture new feeding concept for bull fattening needs a one-page flyer *

We are the innovation leader in the field of cattle feeding in Switzerland. Now we are launching a new “Tarsela” project for cattle fatteners, Munimäster (bull fattening). Tarsela is a complete fattening regime (feed, feed additives, services and advice).
Our sales representatives are with customers every day. You advertise the new project with the aim that our internal specialists get an appointment with the customer for a non-binding presentation of the project. This flyer is intended for this purpose.
Effect:
1. Innovative, modern
2. New
3. emotions
4. technical, scientific

You are also welcome to create a “logo” for Tarsela or choose / design your own lettering.
If you wish to use them, you will also find pictures of such fattening bulls in the appendix. However, pictures are not absolutely necessary.
Size A5, one-sided
Title: TARSELA - for beef fattening professionals
Text:
• Best fattening results
• Top customer service
• Innovative products
• Attractive conditions

Banner or similar:
May we introduce ourselves? or we would be happy to visit you. Etc.

```html
<!DOCTYPE html>
<html lang="en">
<head>
<meta charset="utf-8">
<title>Tarsela – For Beef Fattening Professionals</title>
<link rel="stylesheet" href="https://fonts.googleapis.com/css2?family=Barlow+Condensed:wght@600;700&family=Archivo+Black&display=swap">
<style>
  :root {
    --page-bg: #d9d9d7;
    --wood-dark: #3a1c12;
    --wood-mid: #6a3624;
    --wood-light: #7f4630;
    --header-black: #0b0a0a;
    --brand-red: #cc2417;
    --white: #ffffff;
    --photo-warm: #b07a52;
    --photo-cream: #d9c7a6;
    --photo-steel: #8b949c;
  }
  * { box-sizing: border-box; margin: 0; padding: 0; }
  html, body { width: 1200px; height: 1200px; overflow: hidden; }
  body {
    background: var(--page-bg);
    display: flex; align-items: center; justify-content: center;
    font-family: "Barlow Condensed", "Arial Narrow", sans-serif;
  }
  .flyer {
    position: relative;
    width: 800px; height: 1134px;
    overflow: hidden;
    background:
      repeating-linear-gradient(180deg, rgba(0,0,0,0.18) 0 2px, transparent 2px 19px),
      repeating-linear-gradient(180deg, rgba(255,255,255,0.04) 0 1px, transparent 1px 7px),
      linear-gradient(90deg, var(--wood-dark) 0%, var(--wood-mid) 35%, var(--wood-light) 60%, var(--wood-mid) 85%, var(--wood-dark) 100%);
  }
  .dashed-frame {
    position: absolute; left: 55px; top: 53px; width: 691px; height: 1026px;
    border: 2px dashed rgba(255,255,255,0.85);
  }
  .masthead { position: absolute; left: 93px; top: 0; width: 615px; height: 242px; z-index: 3; }
  .masthead svg { position: absolute; inset: 0; }
  .brand-name {
    position: absolute; left: 0; right: 0; top: 62px;
    text-align: center;
    font-family: "Archivo Black", sans-serif;
    font-size: 84px; letter-spacing: 4px;
    color: var(--white);
    line-height: 1;
  }
  .tagline {
    position: absolute; left: 0; right: 0; top: 170px;
    text-align: center;
    font-size: 30px; font-weight: 700;
    color: var(--brand-red);
    letter-spacing: 0.3px;
  }
  .benefits { position: absolute; left: 151px; top: 285px; list-style: none; z-index: 3; }
  .benefit { display: flex; align-items: center; height: 57px; margin-bottom: 13px; }
  .benefit-marker { width: 57px; height: 57px; background: var(--header-black); flex: none; }
  .benefit-label {
    margin-left: 15px; width: 452px; height: 57px;
    background: var(--brand-red);
    clip-path: polygon(0 0, 100% 0, 94% 100%, 0 100%);
    color: var(--white);
    font-size: 45px; font-weight: 600;
    line-height: 57px; padding-left: 24px;
    letter-spacing: 0.2px;
    white-space: nowrap;
  }
  .photo {
    position: absolute;
    background: var(--white);
    padding: 10px;
    box-shadow: 4px 6px 14px rgba(0,0,0,0.45);
    transform-origin: top left;
    z-index: 1;
  }
  .photo-fill { width: 100%; height: 100%; }
  .photo-feeding-line { left: 436px; top: 566px; width: 420px; height: 292px; transform: rotate(-14deg); }
  .photo-feeding-line .photo-fill { background: linear-gradient(200deg, #7e4a2c 0%, var(--photo-warm) 35%, var(--photo-steel) 60%, #c9b58e 100%); }
  .photo-feeding-row { left: -6px; top: 666px; width: 360px; height: 325px; transform: rotate(-6deg); }
  .photo-feeding-row .photo-fill { background: linear-gradient(160deg, var(--photo-steel) 0%, var(--photo-warm) 40%, var(--photo-cream) 75%, #a08a5a 100%); }
  .photo-bull-closeup { left: 440px; top: 868px; width: 440px; height: 272px; transform: rotate(15deg); z-index: 2; }
  .photo-bull-closeup .photo-fill { background: linear-gradient(120deg, #d8cdb8 0%, var(--photo-cream) 40%, #8a5a3a 70%, #cfc4a8 100%); }
</style>
</head>
<body>
  <main class="flyer">
    <div class="dashed-frame"></div>

    <header class="masthead">
      <svg width="615" height="242" viewBox="0 0 615 242" aria-hidden="true">
        <path d="M0 0 H615 V220 Q307 250 0 220 Z" fill="#0b0a0a"/>
      </svg>
      <h1 class="brand-name">TARSELA</h1>
      <p class="tagline">FOR BEEF FATTENING PROFESSIONALS</p>
    </header>

    <ul class="benefits">
      <li class="benefit"><span class="benefit-marker"></span><span class="benefit-label">BEST FATTENING RESULTS</span></li>
      <li class="benefit"><span class="benefit-marker"></span><span class="benefit-label">TOP CUSTOMER SERVICE</span></li>
      <li class="benefit"><span class="benefit-marker"></span><span class="benefit-label">ATTRACTIVE CONDITIONS</span></li>
      <li class="benefit"><span class="benefit-marker"></span><span class="benefit-label">INNOVATIVE PRODUCTS</span></li>
    </ul>

    <figure class="photo photo-feeding-line">
      <div class="photo-fill" role="img" aria-label="Photo of a long row of Hereford bulls feeding at a barn feed fence"></div>
    </figure>
    <figure class="photo photo-feeding-row">
      <div class="photo-fill" role="img" aria-label="Photo of young bulls eating at a feed rail in a barn"></div>
    </figure>
    <figure class="photo photo-bull-closeup">
      <div class="photo-fill" role="img" aria-label="Close-up photo of a curly-haired fattening bull at the feed trough"></div>
    </figure>
  </main>
</body>
</html>
```